Ad to be used on social media.

____________________________________________________________________________

Bored at Home?

Study to become a
Virtual Mortgage Originator today...

Complete 20 Hour Online Course & State Exam
in 30 days or less

Earn $3,000 to $5,000 on average per loan
No Work Hours, Goals or Quotas
Full Time or Part Time Opportunities

Email us at employment@brightlanehomeloans.com

Brightlane Lending Group, Inc.
7200 Marrowdale Lane
Ellicott City, MD 21043
(800) 417-9062
www.brightlanehomeloans.com
NMLS #837160

```html
<!DOCTYPE html>
<html lang="en">
<head>
<meta charset="utf-8">
<title>Bored at Home? – Brightlane Lending Group</title>
<link rel="stylesheet" href="https://fonts.googleapis.com/css2?family=Roboto+Condensed:ital,wght@0,700;1,700;1,800&family=Arimo:ital,wght@0,400;0,700;1,400;1,700&display=swap">
<style>
  :root {
    --page-bg: #ececec;
    --royal: #0b3aa8;
    --royal-deep: #062a86;
    --royal-light: #1f5ad0;
    --navy: #0b2f8f;
    --headline-gold: #e6cf5a;
    --sand: #e4dcaa;
    --sand-light: #efe9c6;
    --gold: #c6ad45;
    --gold-light: #d9c468;
    --gold-bar: #b99e2f;
    --white: #ffffff;
    --ink: #1d1d1d;
  }
  * { margin: 0; padding: 0; box-sizing: border-box; }
  html, body { width: 1200px; height: 1000px; overflow: hidden; }
  body { background: var(--page-bg); font-family: "Arimo", Arial, sans-serif; position: relative; }

  .ad {
    position: absolute; left: 162px; top: 56px;
    width: 873px; height: 872px; overflow: hidden;
    background: var(--white);
    box-shadow: 0 14px 22px rgba(0,0,0,0.18);
  }
  .ad > * { position: absolute; }

  .hero-band {
    left: 0; top: 0; width: 873px; height: 355px;
    background: linear-gradient(120deg, var(--royal-light) 0%, var(--royal) 45%, var(--royal-deep) 100%);
  }
  .hero-photo { left: 0; top: 0; width: 873px; height: 530px; }

  .headline {
    left: 26px; top: 56px;
    font-family: "Roboto Condensed", "Arial Narrow", sans-serif;
    font-style: italic; font-weight: 800; font-size: 74px; line-height: 1;
    color: var(--headline-gold); letter-spacing: -0.5px;
  }
  .pitch {
    left: 26px; top: 154px; height: 132px;
    border-left: 4px solid var(--white); padding-left: 14px;
    color: var(--white); font-size: 33px; line-height: 42px; letter-spacing: -0.5px;
  }
  .pitch strong { font-style: italic; font-weight: 700; font-size: 35px; }

  .course-chevron { left: 0; top: 355px; width: 410px; height: 175px; }
  .course-note {
    left: 30px; top: 398px;
    color: var(--navy); font-style: italic; font-size: 20px; line-height: 27px;
  }
  .course-note strong { font-weight: 700; font-size: 26px; line-height: 38px; }

  .earn-band {
    left: 0; top: 530px; width: 873px; height: 184px;
    background: linear-gradient(160deg, var(--gold-light) 0%, var(--gold) 55%, var(--gold-light) 100%);
  }
  .cash-photo {
    left: 0; top: 530px; width: 340px; height: 236px;
    background: linear-gradient(150deg, #e8d9c8 0%, #c9d3c0 40%, #9fae98 75%, #d9ddd2 100%);
    clip-path: polygon(0 0, 62% 0, 100% 40%, 90% 100%, 0 100%);
  }
  .earn-line {
    left: 316px; top: 552px; width: 534px; text-align: center;
    color: var(--white); font-weight: 700; font-size: 23px;
  }
  .perks-frame {
    left: 316px; top: 593px; width: 534px; height: 93px;
    border: 2px solid var(--white); border-bottom: none;
  }
  .perks {
    left: 316px; top: 604px; width: 534px; text-align: center;
    font-family: "Roboto Condensed", "Arial Narrow", sans-serif; font-weight: 700;
    color: var(--navy); font-size: 29px; line-height: 32px; letter-spacing: 0.2px;
  }
  .email-line {
    left: 316px; top: 673px; width: 534px; text-align: center;
    color: var(--white); font-size: 19px; line-height: 22px;
  }
  .email-line span { background: transparent; padding: 0 10px; position: relative; }
  .email-line::before, .email-line::after {
    content: ""; position: absolute; top: 11px; height: 2px; width: 46px; background: var(--white);
  }
  .email-line::before { left: 0; }
  .email-line::after { right: 0; }

  .contact {
    left: 38px; display: flex; align-items: center; gap: 12px;
    color: var(--ink); font-size: 22px;
  }
  .contact svg { width: 22px; height: 22px; flex: none; }
  .contact-address { top: 776px; }
  .contact-phone { top: 818px; }
  .contact-phone .web { display: flex; align-items: center; gap: 10px; margin-left: 12px; }

  .brand {
    left: 626px; top: 760px; width: 220px;
    display: flex; flex-direction: column; align-items: center; gap: 8px;
    color: var(--navy); font-weight: 700; font-size: 17px; text-align: center; line-height: 21px;
  }
  .brand-dot { width: 46px; height: 46px; border-radius: 50%; background: var(--gold); }

  .footer-bar { left: 0; top: 862px; width: 873px; height: 10px; background: var(--gold-bar); }
</style>
</head>
<body>
  <main class="ad">
    <div class="hero-band"></div>

    <svg class="hero-photo" viewBox="0 0 873 530" role="img" aria-label="Photo of a woman lying on a bed working on a laptop">
      <defs>
        <linearGradient id="roomTone" x1="0" y1="0" x2="1" y2="1">
          <stop offset="0" stop-color="#3a3c46"/>
          <stop offset="0.45" stop-color="#c9c6c4"/>
          <stop offset="1" stop-color="#eeeeef"/>
        </linearGradient>
      </defs>
      <polygon points="560,0 873,0 873,530 330,530 330,300 470,230" fill="url(#roomTone)"/>
    </svg>

    <h1 class="headline">BORED AT HOME?</h1>
    <p class="pitch">Study to become a<br>Virtual Mortgage Originator<br><strong>TODAY!</strong></p>

    <svg class="course-chevron" viewBox="0 0 410 175" aria-hidden="true">
      <polygon points="0,0 290,0 380,87.5 290,175 0,175" fill="var(--sand)"/>
      <polygon points="300,0 330,0 410,87.5 330,175 300,175 380,87.5" fill="var(--sand-light)" opacity="0.7"/>
    </svg>
    <p class="course-note">Complete 20 Hour Online<br>Course and State Exam In<br><strong>30 DAYS OR LESS!</strong></p>

    <div class="earn-band"></div>
    <div class="cash-photo" role="img" aria-label="Photo of hands fanning out hundred-dollar bills"></div>

    <p class="earn-line">Earn $3,000 to $5,000 on average per loan</p>
    <div class="perks-frame"></div>
    <p class="perks">NO WORK HOURS, GOALS OR QUOTAS<br>FULL TIME OR PART TIME OPPORTUNITIES</p>
    <p class="email-line"><span>email us at employment@brightlanehomeloans.com</span></p>

    <p class="contact contact-address">
      <svg viewBox="0 0 24 24" aria-hidden="true"><path d="M12 2a7 7 0 0 0-7 7c0 5.2 7 13 7 13s7-7.8 7-13a7 7 0 0 0-7-7zm0 9.5A2.5 2.5 0 1 1 12 6.5a2.5 2.5 0 0 1 0 5z" fill="var(--navy)"/></svg>
      7200 Marrowdale Lane, Ellicott City, MD 21043
    </p>
    <p class="contact contact-phone">
      <svg viewBox="0 0 24 24" aria-hidden="true"><path d="M6.6 10.8a15.1 15.1 0 0 0 6.6 6.6l2.2-2.2a1 1 0 0 1 1-.25 11.4 11.4 0 0 0 3.6.57 1 1 0 0 1 1 1V20a1 1 0 0 1-1 1A17 17 0 0 1 3 4a1 1 0 0 1 1-1h3.5a1 1 0 0 1 1 1c0 1.25.2 2.45.57 3.6a1 1 0 0 1-.25 1z" fill="var(--navy)"/></svg>
      (800) 417-9062
      <span class="web">
        <svg viewBox="0 0 24 24" aria-hidden="true"><circle cx="12" cy="12" r="10" fill="none" stroke="var(--navy)" stroke-width="2"/><ellipse cx="12" cy="12" rx="4.5" ry="10" fill="none" stroke="var(--navy)" stroke-width="1.6"/><line x1="2" y1="12" x2="22" y2="12" stroke="var(--navy)" stroke-width="1.6"/></svg>
        www.brightlanehomeloans.com
      </span>
    </p>

    <div class="brand">
      <span class="brand-dot" aria-hidden="true"></span>
      <span>Brightlane Lending Group, Inc.</span>
    </div>

    <div class="footer-bar"></div>
  </main>
</body>
</html>
```